Event Poster - Tarawera Mist Fest 2018 (Need ASAP)

Create a poster for an upcoming vape event, located in Waikato, Hamilton, New Zealand.

Mist Fest is an event where lots of shops come to a location, and the public are welcomed and they all vape, buy vape products, socialize, drink beer and have fun.

VISIT THE EVENT WEBSITE FOR INFO - www.taraweramistfest.co.nz

We have created a website at, as you can see the logo and design is a bit boring and plain, so we dont really want it to look anything like that, The logo that is created to suit the poster will be able to be

Need a poster done up so we can send it around, post it up on boards, share on social media etc

I have attached previous events from nearby towns, for reference, but I want something much better.

Target Market(s)

25-45 Male / Female

Requirements
Must have
• - Tarawera Mist Fest 2018
• - Saturday, 2nd June 2018
• - 12-10pm
• - R18 Event (important for public to know)
• - Vendors, Prizes, Comps, Cloud Liquid Medals, Entertainment, Giveaways & More
• - The Corner Alehouse (14 Moller Ln, Kopuku, Hamilton)
• - mention something along lines "Join Tarawera's Opening Mist Fest"
• - "Grab Your Passes at www.taraweramistfest.co.nz NOW"
• - I want people to know they can buy it from a store as well "The Haze Hut"
Nice to have
• Our City colors are Red,Yellow,Black which is symbolic for "Waikato" so it would be nice to have those integrated in there. Alot of the other Mist Fest events have dark, bogan, amateur look done to them, so I want ours to be just a much better version.
• To Clarify, Hamilton is a city inside the Waikato
• I might want to put sponsors on there as well, possibly 10-20, but maybe only a few if space is a problem

```html
<!DOCTYPE html>
<html lang="en">
<head>
<meta charset="utf-8">
<title>Tarawera Mist Fest 2018 – Event Poster</title>
<link rel="stylesheet" href="https://fonts.googleapis.com/css2?family=Anton&family=Black+Ops+One&family=Lato:wght@400;700&family=Oswald:wght@400;600;700&display=swap">
<style>
  :root {
    --page-bg: #2a2a2a;
    --poster-black: #0b0909;
    --smoke-red: #5a0c0c;
    --smoke-deep: #2b0606;
    --smoke-grey: #3a3634;
    --band-red: #e8120f;
    --title-yellow: #f2c21b;
    --accent-yellow: #f7b50c;
    --bullet-yellow: #f5c518;
    --text-white: #ffffff;
    --pin-red: #e3201b;
  }
  * { margin: 0; padding: 0; box-sizing: border-box; }
  html, body {
    width: 1200px; height: 1200px; overflow: hidden;
    background: var(--page-bg);
  }
  .poster {
    position: absolute; left: 172px; top: 0;
    width: 856px; height: 1200px; overflow: hidden;
    background:
      radial-gradient(ellipse 420px 300px at 120px 330px, rgba(90,12,12,.75), transparent 70%),
      radial-gradient(ellipse 380px 320px at 760px 520px, rgba(90,12,12,.6), transparent 70%),
      radial-gradient(ellipse 360px 260px at 430px 640px, rgba(58,54,52,.45), transparent 70%),
      radial-gradient(ellipse 460px 280px at 600px 1000px, rgba(43,6,6,.9), transparent 70%),
      radial-gradient(ellipse 300px 220px at 160px 900px, rgba(58,54,52,.35), transparent 70%),
      radial-gradient(ellipse 260px 200px at 800px 120px, rgba(120,100,20,.18), transparent 70%),
      var(--poster-black);
    text-align: center;
    color: var(--text-white);
  }
  .line { position: absolute; left: 0; width: 100%; white-space: nowrap; }

  .age-label {
    top: 30px; font-family: "Anton", sans-serif; font-size: 66px;
    letter-spacing: 1px; line-height: 1;
  }
  .event-title {
    top: 118px; font-family: "Black Ops One", sans-serif; font-size: 54px;
    color: var(--title-yellow); line-height: 1; letter-spacing: 1px;
  }
  .event-year {
    top: 180px; font-family: "Black Ops One", sans-serif; font-size: 60px;
    color: var(--title-yellow); line-height: 1;
  }
  .date-band {
    position: absolute; left: 114px; top: 267px; width: 618px; height: 73px;
    background: var(--band-red);
    font-family: "Oswald", sans-serif; font-weight: 700; font-size: 50px;
    color: var(--title-yellow); line-height: 73px; letter-spacing: .5px;
  }
  .date-band sup { font-size: 26px; vertical-align: 20px; line-height: 0; }
  .event-time {
    top: 355px; font-family: "Anton", sans-serif; font-size: 84px; line-height: 1;
  }
  .highlights {
    top: 468px; font-family: "Lato", sans-serif; font-size: 36px; line-height: 50px;
  }
  .highlights .dot { color: var(--bullet-yellow); font-size: 28px; margin: 0 4px 0 10px; }
  .tagline {
    top: 640px; font-family: "Oswald", sans-serif; font-weight: 700; font-size: 40px;
    color: var(--accent-yellow); line-height: 1.2;
  }
  .pass-intro {
    top: 718px; font-family: "Oswald", sans-serif; font-weight: 400; font-size: 32px;
    line-height: 1.2; display: flex; justify-content: center; align-items: center; gap: 18px;
  }
  .pass-intro .rule { width: 82px; height: 2px; background: var(--text-white); }
  .website {
    top: 763px; font-family: "Lato", sans-serif; font-weight: 700; font-size: 38px;
    color: var(--accent-yellow); line-height: 1.2;
  }
  .call-now {
    top: 808px; font-family: "Oswald", sans-serif; font-weight: 700; font-size: 72px; line-height: 1.2;
  }
  .venue-pin { position: absolute; left: 418px; top: 910px; }
  .venue {
    top: 942px; font-family: "Oswald", sans-serif; font-weight: 600; font-size: 24px; line-height: 33px;
  }
  .store-note {
    position: absolute; left: 228px; top: 1063px; width: 190px;
    font-family: "Oswald", sans-serif; font-weight: 600; font-size: 12px;
    line-height: 16px; text-align: left;
  }
  .store-name {
    position: absolute; left: 228px; top: 1122px; width: 150px;
    font-family: "Oswald", sans-serif; font-weight: 400; font-size: 20px;
    line-height: 1; text-align: center;
  }
  .fest-mark {
    position: absolute; left: 460px; top: 1040px;
    display: flex; align-items: center; gap: 14px;
  }
  .fest-mark .mark-square { width: 56px; height: 110px; background: var(--title-yellow); }
  .fest-mark .mark-name {
    font-family: "Oswald", sans-serif; font-weight: 700; font-size: 24px;
    line-height: 26px; color: var(--text-white); text-align: left;
  }
</style>
</head>
<body>
  <main class="poster">
    <p class="line age-label">R18 EVENT</p>
    <h1 class="line event-title">TARAWERA MIST FEST</h1>
    <p class="line event-year">2018</p>

    <p class="date-band">SATURDAY 2<sup>ND</sup> JUNE 2018</p>
    <p class="line event-time">12-10PM</p>

    <p class="line highlights">
      <span class="dot">●</span>Vendors, <span class="dot">●</span>Prizes, <span class="dot">●</span>Comps, <span class="dot">●</span>Cloud Liquid<br>
      Medals, <span class="dot">●</span>Entertainment,<br>
      <span class="dot">●</span>Giveaways &amp; More
    </p>

    <p class="line tagline">JOIN TARAWERA'S OPENING MIST FEST</p>
    <p class="line pass-intro"><span class="rule"></span>Grab Your Passes at<span class="rule"></span></p>
    <p class="line website">www.taraweramistfest.co.nz</p>
    <p class="line call-now">NOW</p>

    <svg class="venue-pin" width="20" height="22" viewBox="0 0 20 22" aria-hidden="true">
      <path d="M10 1a7 7 0 0 0-7 7c0 5 7 13 7 13s7-8 7-13a7 7 0 0 0-7-7z" fill="var(--pin-red)" stroke="#fff" stroke-width="1.5"/>
      <circle cx="10" cy="8" r="2.5" fill="#fff"/>
    </svg>
    <p class="line venue">THE CORNER ALEHOUSE<br>(14 MOLLER LN, KOPUKU, HAMILTON)</p>

    <p class="store-note">YOU CAN ALSO PURCHASE<br>YOUR TICKET INSTORE AT:</p>
    <p class="store-name">THE HAZE HUT</p>

    <div class="fest-mark">
      <span class="mark-square"></span>
      <p class="mark-name">TARAWERA<br>MIST<br>FEST<br>2018</p>
    </div>
  </main>
</body>
</html>
```